2018 Vision Board Workshop

I need to promote this workshop on both an 8.5x11 sheet and a 5x7 card. I do have a logo that needs to be present. I'd like to stay true to my branded colors. The flyer needs to project the excitement of a new year and the possibilities of what a person can create, produce, explore in their lives by putting it all on a vision board. Creating the vision of what you want will inspire you to achieve your goals and dreams. Looking at your vision board each day will propel you into taking action as you chart your course to achieve what you truly want.
The flyer needs to have the following information:
The workshop date and time - Sat., Jan. 13, 2018, 10:30-1:30
The location is - Atrium 47B, 2864 Birchwood Vale Rd, Colorado Springs, Co 80417
in the FORGE Room
My name and contact information - Mara Vollbeck
Text and voice 303-417-6652
Email - mara@brightwell-daily-craft.com
Website - brightwell-daily-craft.com
The fee is $45. All materials are provided.

My company is called Brightwell Daily Craft. I am a Life Coach, author, speaker and workshop leader.\ I wrote this program, Brightwell Daily Craft to teach concepts and supporting skills for living with more happiness, satisfaction and fulfillment. Thanks for reading this!! Mara

Target Market(s)

Primarily women, educated, motivated, proactive in their own lives and well being

Font styles to use
Other font styles liked:
• I have been using Century Gothic. I'm open to new ideas.

Requirements
Must have
• The Brightwell Daily Craft logo
• The flyer needs to have the following information:
• The workshop date and time - Sat., Jan. 13, 2018, 10:30-1:30
• The location is - Atrium 47B, 2864 Birchwood Vale Rd, Colorado Springs, Co 80417
• in the FORGE Room
• My name and contact information - Mara Vollbeck
• Text and voice 303-417-6652
• Email - mara@brightwell-daily-craft.com
• Website - brightwell-daily-craft.com
• The fee is $45. All materials are provided.
Nice to have
• The Brightwell Daily Craft branded colors in the design
• Images of vision boards

```html
<!DOCTYPE html>
<html lang="en">
<head>
<meta charset="utf-8">
<title>2018 Vision Board Workshop with Mara</title>
<link href="https://fonts.googleapis.com/css2?family=Montserrat:wght@600;700&family=Didact+Gothic&display=swap" rel="stylesheet">
<style>
  :root {
    --blue: #3fa9e0;
    --green: #8dc63f;
    --white: #ffffff;
    --paper: #fbfbf8;
    --cork-light: #d4b48a;
    --cork-dark: #b8946a;
    --tape-blue: rgba(63,169,224,.75);
    --tape-green: rgba(141,198,63,.8);
    --photo-sea: #6f93a3;
    --photo-pier: #b9773a;
    --photo-stairs: #c9d3cf;
    --photo-portrait: #d9b57a;
  }
  * { margin: 0; padding: 0; box-sizing: border-box; }
  html, body { width: 927px; height: 1200px; overflow: hidden; background: var(--white); }
  body { font-family: "Didact Gothic", "Century Gothic", sans-serif; }
  .flyer { position: relative; width: 927px; height: 1200px; overflow: hidden; background: var(--white); }
  .abs { position: absolute; }

  .corkboard { left: 0; top: 0; width: 927px; height: 668px;
    background: radial-gradient(circle at 40% 30%, var(--cork-light), var(--cork-dark)); }

  .paper { position: absolute; background: var(--paper); box-shadow: 0 2px 4px rgba(0,0,0,.25);
    display: flex; align-items: center; justify-content: center; }
  .tape { position: absolute; height: 14px; width: 70px; }
  .tape.blue { background: var(--tape-blue); }
  .tape.green { background: var(--tape-green); }

  .headline { font-family: "Montserrat", "Century Gothic", sans-serif; font-weight: 700; line-height: 1; }
  .headline.year { color: var(--blue); font-size: 96px; }
  .headline.vision { color: var(--green); font-size: 74px; letter-spacing: -1px; }
  .headline.workshop { color: var(--blue); font-size: 76px; letter-spacing: -1px; }

  .word { font-family: "Didact Gothic", "Century Gothic", sans-serif; font-size: 36px; }
  .word.green { color: var(--green); }
  .word.blue { color: var(--blue); }

  .host-tag { left: 468px; top: 344px; width: 234px; height: 72px; background: var(--blue);
    transform: rotate(-6deg); color: var(--white); font-family: "Montserrat", sans-serif; font-weight: 600;
    font-size: 34px; display: flex; align-items: center; justify-content: center; }

  .photo { position: absolute; box-shadow: 0 2px 5px rgba(0,0,0,.3); }
  .photo.sea { left: 8px; top: 364px; width: 304px; height: 252px; background: var(--photo-sea); }
  .photo.pier { left: 328px; top: 370px; width: 284px; height: 244px; background: var(--photo-pier); }
  .photo.stairs { left: 620px; top: 356px; width: 292px; height: 300px; background: var(--photo-stairs); }

  .info-panel { left: 492px; top: 668px; width: 420px; height: 276px; background: var(--green); }
  .info-panel p { color: var(--white); font-size: 21px; line-height: 27px; }
  .info-panel b { font-family: "Montserrat", sans-serif; font-weight: 700; font-size: 18px; }
  .fee-badge { left: 662px; top: 866px; width: 252px; height: 174px; border-radius: 50%;
    background: var(--white); border: 4px solid var(--green); }
  .fee-text { left: 676px; top: 902px; width: 230px; text-align: center; transform: rotate(-10deg);
    color: var(--blue); font-family: "Montserrat", sans-serif; font-weight: 700; font-size: 31px; line-height: 38px; }

  .band { position: absolute; background: var(--blue); color: var(--white); display: flex; align-items: center; }
  .date-band { left: 28px; top: 694px; width: 480px; height: 58px; padding-left: 22px; font-size: 36px;
    clip-path: polygon(0 0, 100% 0, 98% 100%, 2% 100%); }
  .date-band b { font-family: "Montserrat", sans-serif; font-weight: 600; margin-right: 12px; }
  .name-band { left: 18px; top: 778px; width: 286px; height: 46px; padding-left: 24px; font-size: 26px;
    clip-path: polygon(0 0, 100% 0, 100% 100%, 3% 100%); }
  .roles { left: 40px; top: 840px; color: var(--green); font-size: 22px; line-height: 29px; }
  .portrait { left: 260px; top: 766px; width: 184px; height: 184px; border-radius: 50%;
    border: 5px solid var(--blue); background: var(--photo-portrait); }

  .brand { left: 72px; top: 1030px; width: 340px; display: flex; align-items: center; gap: 10px; }
  .brand-dot { width: 24px; height: 24px; border-radius: 50%; background: var(--green); flex: none; }
  .brand-name { color: var(--green); font-size: 30px; }
  .website { left: 90px; top: 1097px; color: var(--green); font-family: "Montserrat", sans-serif; font-weight: 600; font-size: 18px; }
  .contact { left: 512px; top: 1064px; color: var(--blue); font-size: 19px; line-height: 27px; }

  .footer { left: 0; top: 1144px; width: 927px; height: 56px; background: var(--green); color: var(--white);
    font-size: 22px; display: flex; align-items: center; justify-content: center; }
</style>
</head>
<body>
<main class="flyer">
  <div class="abs corkboard" role="img" aria-label="Cork board texture background"></div>

  <div class="paper" style="left:56px;top:48px;width:184px;height:80px;transform:rotate(3deg)"><span class="word green">DREAMS</span></div>
  <div class="tape blue" style="left:116px;top:40px;transform:rotate(8deg)"></div>
  <div class="paper" style="left:712px;top:48px;width:160px;height:64px;transform:rotate(2deg)"><span class="word blue">GOALS</span></div>
  <div class="tape blue" style="left:762px;top:42px;transform:rotate(6deg)"></div>

  <div class="paper" style="left:292px;top:56px;width:364px;height:112px"><span class="headline year">2018</span></div>
  <div class="paper" style="left:148px;top:166px;width:644px;height:90px"><span class="headline vision">VISION BOARD</span></div>
  <div class="paper" style="left:212px;top:264px;width:500px;height:84px"><span class="headline workshop">WORKSHOP</span></div>

  <div class="paper" style="left:52px;top:280px;width:152px;height:72px;transform:rotate(-8deg)"><span class="word blue">feel</span></div>
  <div class="tape green" style="left:80px;top:274px;transform:rotate(-4deg)"></div>
  <div class="paper" style="left:756px;top:280px;width:156px;height:72px;transform:rotate(8deg)"><span class="word blue">Create</span></div>
  <div class="tape green" style="left:808px;top:270px;transform:rotate(10deg)"></div>

  <div class="photo sea" role="img" aria-label="Photo of a joyful woman with raised arms by the sea"></div>
  <div class="photo pier" role="img" aria-label="Photo of a wooden pier leading toward the sunset"></div>
  <div class="photo stairs" role="img" aria-label="Photo looking down a white spiral staircase around green foliage"></div>
  <div class="tape blue" style="left:110px;top:352px;width:100px;transform:rotate(4deg)"></div>
  <div class="tape green" style="left:420px;top:364px;width:52px;transform:rotate(4deg)"></div>
  <div class="tape blue" style="left:704px;top:352px;width:100px"></div>

  <div class="abs host-tag">with Mara</div>

  <div class="paper" style="left:132px;top:584px;width:148px;height:66px;transform:rotate(-3deg)"><span class="word green">joy</span></div>
  <div class="paper" style="left:412px;top:598px;width:160px;height:64px;transform:rotate(1deg)"><span class="word green" style="font-size:33px">Explore</span></div>
  <div class="paper" style="left:724px;top:596px;width:172px;height:66px;transform:rotate(-5deg)"><span class="word green">Climb</span></div>
  <div class="tape green" style="left:770px;top:590px;width:60px"></div>

  <section class="abs info-panel">
    <div style="position:absolute;left:44px;top:42px">
      <p><b>Time:</b> 10:30-1:30</p>
      <p style="margin-top:10px"><b>Location:</b> Atrium 47B,<br>2864 Birchwood Vale Rd,<br>Colorado Springs, Co 80417<br>in the FORGE Room</p>
    </div>
  </section>
  <div class="abs fee-badge"></div>
  <div class="abs fee-text">Registration<br>Fee: $45</div>

  <div class="band date-band"><b>Date :</b> Sat., Jan. 13. 2018</div>
  <div class="band name-band">Mara Vollbeck</div>
  <p class="abs roles">Author, Coach,<br>Speaker and<br>Workshop Leader</p>
  <div class="abs portrait" role="img" aria-label="Portrait photo of workshop leader Mara Vollbeck"></div>

  <div class="abs brand"><span class="brand-dot"></span><span class="brand-name">Brightwell Daily Craft</span></div>
  <p class="abs website">www.brightwell-daily-craft.com</p>

  <p class="abs contact">Text and voice 303-417-6652<br>Email - mara@brightwell-daily-craft.com</p>

  <footer class="abs footer">All materials are provided</footer>
</main>
</body>
</html>
```